Trucking company specializing in intermodal containers

We need a logo design for our trucking company based in Kent, Washington. Our companies name is Dorvale Haulworks LLC, we specialize in intermodal containers, and work off of the Crestmark rail lines and the ports. We provide service by transporting freight with our fleet of trucks. We operate within Washington, Oregon, and Idaho. Our fleet consists of an east division and a local division. Our team motto currently is globally connected, locally invested.

Target Market(s)

brokers, intermodal management companies, customers

Industry/Entity Type

Trucking Company

Contact Information for Business Card

physical address 4519 N. 163rd Pl Kent, WA 98517
office number is 253-614-9026

Font styles to use
Sans Serif

Colors

Designer to choose colors to be used in the design.

Requirements
Must have
• We need to update our current logo. Something like an emblem; that makes a statement that this logo/ sign represents Dorvale Haulworks. Something like a royal stamp but in this case a royal shield.
Nice to have
• simple, yet bold. something someone does not currently have. We need something fresh and exciting. Something that will also make a statement because currently our reputation is great within the industry and our community. But we need to reflect that we are professional and willing to provide the best service. We are open to new statement lines.
Should not have
• Should not have something thats been used before. We are open to suggestions that you have and a design that is completely unique and you make originally without what we want but what you like as well. Ofcourse it should still represent the industry we are in.

```html
<!DOCTYPE html>
<html lang="en">
<head>
<meta charset="utf-8">
<title>Dorvale Haulworks LLC — Business Card</title>
<link rel="stylesheet" href="https://fonts.googleapis.com/css2?family=Cinzel:wght@600&family=Open+Sans:wght@400;600;700&display=swap">
<style>
  :root {
    --backdrop: #3b3431;
    --card: #111010;
    --card-edge: #1d1b1b;
    --gold: #eaa416;
    --gold-soft: #b37c12;
    --ink: #f2f2f2;
    --silver: #b9b9bb;
    --circle-red: #8e1214;
  }
  * { box-sizing: border-box; margin: 0; padding: 0; }
  html, body {
    width: 1200px;
    height: 900px;
    overflow: hidden;
    background: var(--backdrop);
  }
  .canvas {
    position: relative;
    width: 1200px;
    height: 900px;
    font-family: "Open Sans", sans-serif;
  }
  .card {
    position: absolute;
    top: 300px;
    width: 520px;
    height: 300px;
    background: var(--card);
    border: 1px solid var(--card-edge);
    box-shadow: 0 14px 30px rgba(0,0,0,.45);
  }
  .card--contact { left: 60px; }
  .card--brand { left: 620px; }

  /* contact side */
  .contact-mark {
    position: absolute;
    left: 30px;
    top: 0;
    width: 190px;
    height: 300px;
    display: flex;
    align-items: center;
    gap: 12px;
  }
  .mark-dot {
    flex: none;
    width: 34px;
    height: 34px;
    border-radius: 50%;
    background: var(--circle-red);
  }
  .mark-name {
    color: var(--ink);
    font-weight: 700;
    font-size: 19px;
    line-height: 1.2;
  }
  .divider {
    position: absolute;
    left: 232px;
    top: 70px;
    width: 1px;
    height: 160px;
    background: linear-gradient(to bottom, transparent, var(--gold-soft) 30%, var(--gold-soft) 70%, transparent);
  }
  .details {
    position: absolute;
    left: 256px;
    top: 82px;
    color: var(--ink);
  }
  .person-name {
    font-family: "Cinzel", serif;
    font-weight: 600;
    font-size: 18px;
    color: var(--gold);
    letter-spacing: .5px;
  }
  .person-role {
    font-size: 12.5px;
    margin-top: 1px;
  }
  .contact-list {
    list-style: none;
    margin-top: 18px;
    font-size: 13px;
    line-height: 21px;
  }
  .contact-list li {
    display: flex;
    align-items: center;
    gap: 8px;
  }
  .contact-list svg {
    width: 11px;
    height: 11px;
    fill: var(--gold);
    flex: none;
  }
  .address {
    margin-top: 14px;
    font-size: 13px;
  }

  /* brand side */
  .brand-lockup {
    position: absolute;
    inset: 0;
    display: flex;
    align-items: center;
    justify-content: center;
    gap: 16px;
  }
  .brand-dot {
    width: 46px;
    height: 46px;
    border-radius: 50%;
    background: var(--silver);
  }
  .brand-name {
    color: var(--silver);
    font-weight: 700;
    font-size: 30px;
    line-height: 1.1;
  }
</style>
</head>
<body>
<main class="canvas">
  <section class="card card--contact">
    <div class="contact-mark">
      <span class="mark-dot"></span>
      <span class="mark-name">Dorvale Haulworks LLC</span>
    </div>
    <span class="divider"></span>
    <div class="details">
      <p class="person-name">MARCUS HALE</p>
      <p class="person-role">Managing Director</p>
      <ul class="contact-list">
        <li>
          <svg viewBox="0 0 24 24" aria-hidden="true"><path d="M6.6 10.8a15.1 15.1 0 0 0 6.6 6.6l2.2-2.2c.3-.3.7-.4 1-.2 1.1.4 2.3.6 3.6.6.6 0 1 .4 1 1V20c0 .6-.4 1-1 1A17 17 0 0 1 3 4c0-.6.4-1 1-1h3.5c.6 0 1 .4 1 1 0 1.3.2 2.5.6 3.6.1.3 0 .7-.2 1z"/></svg>
          253-614-9026
        </li>
        <li>
          <svg viewBox="0 0 24 24" aria-hidden="true"><path d="M2 5h20v14H2z M2 5l10 8 10-8" /><path d="M3 6.5l9 7 9-7V18H3z" fill="#111010"/></svg>
          info@dorvalehaulworks.com
        </li>
        <li>
          <svg viewBox="0 0 24 24" aria-hidden="true"><circle cx="12" cy="12" r="10"/><path d="M2 12h20M12 2c3 3 3 17 0 20M12 2c-3 3-3 17 0 20" stroke="#111010" stroke-width="1.6" fill="none"/></svg>
          www.dorvalehaulworks.com
        </li>
      </ul>
      <p class="address">4519 N. 163rd Pl Kent, WA 98517</p>
    </div>
  </section>

  <section class="card card--brand">
    <div class="brand-lockup">
      <span class="brand-dot"></span>
      <span class="brand-name">Dorvale Haulworks LLC</span>
    </div>
  </section>
</main>
</body>
</html>
```